Advertisement Coaching practice

I need an advertisement (to be printed in newspaper). I have a coaching practice where I offer coaching, workshops family constellations and relationship therapy. The ad needs to express calmness, inspiration to transform but also not dull and boring. It would be great if you could use the colors from my logo into the ad.

Dimensions are: 13,04 cm Width x 9,72 cm Height.

I will add my previous self-made ad, my company logo, a portrait photo of myself and the text I want to add. Also my contact details should be visible as well.

Requirements
Nice to have
• I have updated the brief with a flyer that I had previously made by a designer. It would be a nice to have if the ad ties in with that. You can also look at my website at www.fernbrook.nu to see what colors I used there.

```html
<!DOCTYPE html>
<html lang="nl">
<head>
<meta charset="utf-8">
<title>Fernbrook – Coaching advertentie</title>
<link href="https://fonts.googleapis.com/css2?family=Poppins:wght@400;500;600;700&display=swap" rel="stylesheet">
<style>
  :root{
    --page:#eef0f3;
    --white:#ffffff;
    --ink:#1e1e22;
    --grey:#55565c;
    --lilac:#b088c4;
    --navy:#1f5a82;
    --coral:#ee6b5a;
    --blue:#1f6896;
    --orange:#f29a1f;
    --purple:#9a63bb;
  }
  *{box-sizing:border-box;margin:0;padding:0}
  html,body{width:1200px;height:900px;overflow:hidden;background:var(--page);font-family:"Poppins",sans-serif}
  .ad{position:absolute;left:20px;top:17px;width:1160px;height:865px;background:var(--white);overflow:hidden}
  .family-photo{position:absolute;left:509px;top:0;width:651px;height:471px;
    background:linear-gradient(90deg,#ffffff 0%,rgba(255,255,255,0) 30%),
               linear-gradient(160deg,#f6e6cf 0%,#d8a57e 40%,#8d6a55 75%,#b9aca2 100%)}
  .brand{position:absolute;left:63px;top:48px;width:220px;text-align:center}
  .brand-dot{width:72px;height:72px;border-radius:50%;border:3px solid var(--grey);margin:0 auto 6px}
  .brand-name{font-size:40px;font-weight:400;color:var(--grey);line-height:1.1;letter-spacing:1px}
  .headline-line{position:absolute;font-weight:700;line-height:1;white-space:nowrap}
  .headline-main{left:45px;top:225px;font-size:76px;color:var(--lilac);letter-spacing:-1px}
  .headline-sub{left:50px;top:294px;font-size:48px;color:var(--navy);letter-spacing:-.5px}
  .headline-accent{left:50px;top:341px;font-size:48px;color:var(--coral);letter-spacing:-.5px}
  .intro{position:absolute;left:51px;top:400px;width:620px;font-size:17.5px;font-weight:500;color:var(--ink);line-height:22px;white-space:nowrap}
  .lower{position:absolute;left:0;top:471px;width:1160px;height:394px;background:var(--blue)}
  .lower-edge{position:absolute;left:0;top:469px;width:1160px;height:3px;background:var(--coral)}
  .intro-band{position:absolute;left:0;top:471px;width:698px;height:58px;background:var(--coral);border-radius:0 0 26px 0;
    color:var(--white);font-weight:700;font-size:25px;line-height:58px;padding-left:53px;letter-spacing:-.2px;white-space:nowrap}
  .portrait{position:absolute;left:851px;top:411px;width:309px;height:454px;
    background:linear-gradient(90deg,var(--blue) 0%,rgba(31,104,150,0) 22%),
               radial-gradient(ellipse at 55% 35%,#b98466 0%,#6f4a3a 40%,#aebbd0 75%,#c9d3e2 100%)}
  .benefit{position:absolute;display:flex;align-items:center;gap:12px;color:var(--white);font-size:19px;line-height:22px;white-space:nowrap}
  .benefit svg{flex:none}
  .benefit-patterns{left:56px;top:555px}
  .benefit-conflicts{left:300px;top:555px}
  .benefit-connection{left:549px;top:555px}
  .offer{position:absolute;left:53px;top:642px;width:760px;color:var(--white);font-size:17px;line-height:20.7px;white-space:nowrap}
  .divider{position:absolute;left:53px;top:744px;width:702px;border-top:1.5px dashed rgba(255,255,255,.85)}
  .contact{position:absolute;left:53px;top:765px;display:flex;gap:22px;color:var(--white);font-size:15.5px;font-weight:500;align-items:center}
  .contact span{display:flex;align-items:center;gap:6px}
  .website{position:absolute;left:53px;top:788px;color:var(--white);font-size:26px;font-weight:600;letter-spacing:5px}
  .name-tag{position:absolute;left:416px;top:764px;width:367px;height:58px;background:var(--purple);border-radius:10px 0 0 10px;
    color:var(--white);font-weight:700;font-size:31px;line-height:58px;padding-left:20px;white-space:nowrap}
</style>
</head>
<body>
<div class="ad">
  <div class="family-photo" role="img" aria-label="Foto van een lachend gezin dat elkaar omhelst in een zonnige woonkamer"></div>

  <div class="brand">
    <div class="brand-dot"></div>
    <div class="brand-name">fernbrook</div>
  </div>

  <div class="headline-line headline-main">COACHING</div>
  <div class="headline-line headline-sub">FAMILIEOPSTELLINGEN</div>
  <div class="headline-line headline-accent">&amp; RELATIETHERAPIE</div>

  <p class="intro">Trauma’s en negatieve ervaringen vormen ons en blijven nog<br>lang voelbaar. Ze kunnen groei of geluk in de weg staan.</p>

  <div class="lower"></div>
  <div class="lower-edge"></div>
  <div class="portrait" role="img" aria-label="Portretfoto van de coach in een lichtblauwe blouse"></div>
  <div class="intro-band">IK BEN MARIEKE EN ONDERSTEUN JE BIJ HET:</div>

  <div class="benefit benefit-patterns">
    <svg width="62" height="62" viewBox="0 0 62 62"><circle cx="31" cy="31" r="28" fill="#fff" stroke="#f29a1f" stroke-width="4"/><path d="M17 44h8v-7h8v-7h8v-7h6" fill="none" stroke="#1f5a82" stroke-width="3.5" stroke-linejoin="round"/></svg>
    <div>Doorbreken van<br>belemmerende<br>patronen;</div>
  </div>
  <div class="benefit benefit-conflicts">
    <svg width="62" height="62" viewBox="0 0 62 62"><circle cx="31" cy="31" r="28" fill="#fff" stroke="#f29a1f" stroke-width="4"/><path d="M18 24h26M18 24l4-4M18 24l4 4M44 24l-4-4M44 24l-4 4" fill="none" stroke="#1f5a82" stroke-width="2.5" stroke-linecap="round"/><circle cx="25" cy="37" r="6" fill="#1f5a82"/><circle cx="37" cy="37" r="6" fill="#1f5a82"/></svg>
    <div>Beter omgaan<br>met conflicten;</div>
  </div>
  <div class="benefit benefit-connection">
    <svg width="62" height="62" viewBox="0 0 62 62"><circle cx="31" cy="31" r="28" fill="#fff" stroke="#f29a1f" stroke-width="4"/><g stroke="#1f5a82" stroke-width="2.5"><line x1="31" y1="31" x2="19" y2="19"/><line x1="31" y1="31" x2="43" y2="19"/><line x1="31" y1="31" x2="19" y2="43"/><line x1="31" y1="31" x2="43" y2="43"/><line x1="31" y1="31" x2="31" y2="15"/></g><g fill="#1f5a82"><circle cx="31" cy="31" r="6"/><circle cx="19" cy="19" r="3.5"/><circle cx="43" cy="19" r="3.5"/><circle cx="19" cy="43" r="3.5"/><circle cx="43" cy="43" r="3.5"/><circle cx="31" cy="15" r="3"/></g></svg>
    <div>In gezonde verbinding<br>met elkaar als koppel of<br>met anderen komen;</div>
  </div>

  <p class="offer">Maandelijks geef ik workshops familieopstellingen. Ook houd ik themasessies rond<br>adoptie, moeder-dochterdynamiek of relaties. Ook bied ik individuele coaching,<br>relatietherapie en retraites aan. Kijk op de website voor meer info of neem contact op<br>en ontdek wat het beste bij jou past.</p>

  <div class="divider"></div>

  <div class="contact">
    <span><svg width="15" height="15" viewBox="0 0 24 24"><path d="M6.6 10.8a15 15 0 0 0 6.6 6.6l2.2-2.2c.3-.3.7-.4 1-.2 1.1.4 2.3.6 3.6.6.6 0 1 .4 1 1V20c0 .6-.4 1-1 1A17 17 0 0 1 3 4c0-.6.4-1 1-1h3.5c.6 0 1 .4 1 1 0 1.3.2 2.5.6 3.6.1.3 0 .7-.2 1z" fill="#f29a1f"/></svg>06-12 34 56 78</span>
    <span><svg width="17" height="13" viewBox="0 0 24 18"><rect x="1" y="1" width="22" height="16" rx="1.5" fill="#f29a1f"/><path d="M2 2l10 8 10-8" fill="none" stroke="#1f6896" stroke-width="1.8"/></svg>info@fernbrook.nu</span>
  </div>
  <div class="website">www.fernbrook.nu</div>

  <div class="name-tag">MARIEKE DALEN</div>
</div>
</body>
</html>
```